Real Estate Investing company needs a business card design

We need a business card design for new Real Estate Investment Company called "Brightgate Holdings, LLC." We buy homes for cash and close quickly in any situation. Our company provides an easy and fast option for home owners who are in tough situations who need to sell their home fast and don't want realtor fees or other listing hassles. We also renovate and resell our homes which helps provide housing for the community. We would like to see designs that use the colors blue and white to match our company logo or other colors that may match our company logo. The final design should communicate trust and easy process.
Industry/Entity Type
Business
Contact Information for Business Card
Front should have company name and company logo. back of card should have company logo and area to list services.
Look and feel

```html
<!DOCTYPE html>
<html lang="en">
<head>
<meta charset="UTF-8">
<title>Brightgate Holdings – Business Card</title>
<link href="https://fonts.googleapis.com/css2?family=Open+Sans:wght@400;600;700&display=swap" rel="stylesheet">
<style>
  :root {
    --backdrop: #e6e4e2;
    --card: #141414;
    --card-edge: #1c1c1c;
    --spot-gloss: #2b2b2b;
    --brand-blue: #1f7fd6;
    --text-light: #f2f2f2;
    --text-muted: #c9c9c9;
    --divider: #333333;
  }
  * { margin: 0; padding: 0; box-sizing: border-box; }
  html, body {
    width: 1200px;
    height: 716px;
    overflow: hidden;
    background: var(--backdrop);
    font-family: "Open Sans", Arial, sans-serif;
  }
  .canvas {
    position: relative;
    width: 1200px;
    height: 716px;
    display: flex;
    align-items: center;
    justify-content: center;
    gap: 50px;
  }
  .card {
    position: relative;
    width: 525px;
    height: 300px;
    background: var(--card);
    border: 1px solid var(--card-edge);
    border-radius: 3px;
    box-shadow: 0 6px 18px rgba(0,0,0,0.25);
  }
  /* Front */
  .card-front {
    display: flex;
    align-items: center;
    justify-content: center;
  }
  .wordmark-front {
    font-weight: 700;
    font-size: 34px;
    line-height: 1.05;
    text-transform: uppercase;
    letter-spacing: 1px;
    color: var(--spot-gloss);
    text-align: center;
  }
  /* Back */
  .card-back {
    display: flex;
  }
  .brand-panel {
    width: 56%;
    display: flex;
    align-items: center;
    justify-content: center;
    border-right: 1px solid var(--divider);
    margin: 40px 0;
  }
  .wordmark-back {
    display: flex;
    align-items: center;
    gap: 10px;
    font-weight: 700;
    font-size: 24px;
    line-height: 1.05;
    text-transform: uppercase;
    color: var(--brand-blue);
  }
  .brand-square {
    width: 14px;
    height: 14px;
    background: var(--brand-blue);
    flex-shrink: 0;
  }
  .contact-panel {
    flex: 1;
    padding: 0 22px;
    display: flex;
    flex-direction: column;
    justify-content: center;
    color: var(--text-light);
  }
  .person-name {
    font-weight: 600;
    font-size: 19px;
    letter-spacing: 0.5px;
  }
  .person-title {
    font-size: 10px;
    color: var(--text-muted);
    margin-bottom: 16px;
  }
  .contact-line {
    display: flex;
    align-items: center;
    gap: 8px;
    font-size: 11px;
    margin-bottom: 5px;
  }
  .contact-icon { width: 11px; height: 11px; flex-shrink: 0; }
  .address {
    font-size: 11px;
    line-height: 1.45;
    margin-top: 2px;
  }
</style>
</head>
<body>
<main class="canvas">
  <section class="card card-front" aria-label="Card front">
    <div class="wordmark-front">Brightgate<br>Holdings</div>
  </section>

  <section class="card card-back" aria-label="Card back">
    <div class="brand-panel">
      <div class="wordmark-back">
        <span class="brand-square"></span>
        <span>Brightgate<br>Holdings</span>
      </div>
    </div>
    <div class="contact-panel">
      <p class="person-name">YOUR NAME</p>
      <p class="person-title">Managing Director</p>
      <p class="contact-line">
        <svg class="contact-icon" viewBox="0 0 12 12" aria-hidden="true">
          <path d="M2.5 1h2l1 2.5-1.3 1a6 6 0 0 0 3.3 3.3l1-1.3L11 7.5v2A1.5 1.5 0 0 1 9.5 11 8.5 8.5 0 0 1 1 2.5 1.5 1.5 0 0 1 2.5 1z" fill="#1f7fd6"/>
        </svg>
        +00 111 222 3333
      </p>
      <p class="contact-line">
        <svg class="contact-icon" viewBox="0 0 12 12" aria-hidden="true">
          <rect x="1" y="2.5" width="10" height="7" rx="1" fill="#1f7fd6"/>
          <path d="M1.5 3.2 6 6.5l4.5-3.3" fill="none" stroke="#141414" stroke-width="1"/>
        </svg>
        yourname@brightgateholdings.com
      </p>
      <p class="address">Your Long Commercial or<br>business address in 2 line</p>
    </div>
  </section>
</main>
</body>
</html>
```